Brevin K - Premium Business Cards

Background of Brevin K
Brevin Kaltwell is a cigar mobile lounge where guests become family. A place of luxury, relaxation, and ambiance is the global popularity demand. Brevin Kaltwell strives to provide first-class service of quality and products. Our goal is to ensure that every guest is treated and serviced as a VIP.

Brevin Kaltwell was founded by Dennis Marlow Jr in January 2020. After 15 years of cigar reviews and research Dennis decided it was time to launch his own cigar brand and boutique cigar company. With a wealth of knowledge and years of experience Brevin Kaltwell was born. With opulence for all cultures, Brevin Kaltwell offers hand rolled cigars with premium blend tobacco from sweet to bold imported from Costa Rica, Dominican Republic, and Nicaragua. Thank you for your business!

Objective:
Create a business card template to be used for all employees. Design should communicate premium and classy. And should use earth tone colors.

Design should include:
1. Client wants to incorporate the cigar leaf
2. Logo
3. Tagline: Respect the smoke
3. Content info:
Calvin Rusholm
Owner
614-587-3906
crusholm@brevinleafco.com
brevinkaltwell.com

```html
<!DOCTYPE html>
<html lang="en">
<head>
<meta charset="utf-8">
<title>Brevin K – Business Cards</title>
<link href="https://fonts.googleapis.com/css2?family=Montserrat:wght@400;500;700;800&display=swap" rel="stylesheet">
<style>
  :root {
    --stage: #2a241f;
    --card-dark: #3a291d;
    --paper: #f4ece0;
    --ink: #2e2118;
    --ink-soft: #5b4636;
    --band: #5a3e2b;
    --band-text: #eadbc4;
    --rule: #a58a6c;
    --leaf-light: #c49a5e;
    --leaf-dark: #7a5a34;
  }
  * { margin: 0; padding: 0; box-sizing: border-box; }
  html, body { width: 1200px; height: 1186px; overflow: hidden; }
  body {
    background: var(--stage);
    font-family: "Montserrat", sans-serif;
    position: relative;
  }
  .card {
    position: absolute;
    left: 190px;
    width: 820px;
    height: 469px;
    border-radius: 30px;
    overflow: hidden;
  }
  .card--back { top: 92px; background: var(--card-dark); }
  .card--front { top: 625px; background: var(--paper); }

  .leaf-art {
    position: absolute;
    left: 50%;
    transform: translateX(-50%);
    width: 300px;
    height: 56px;
    border-radius: 28px;
    background: linear-gradient(90deg, var(--leaf-dark), var(--leaf-light) 55%, var(--leaf-dark));
    opacity: .85;
  }
  .card--back .leaf-art { top: 130px; }
  .card--front .leaf-art { top: 34px; }

  .brand {
    position: absolute;
    left: 0; right: 0;
    text-align: center;
    font-weight: 800;
    letter-spacing: 1px;
    font-size: 62px;
    line-height: 1;
  }
  .card--back .brand { top: 214px; color: var(--paper); }
  .card--front .brand { top: 112px; color: var(--ink); }

  .band {
    position: absolute;
    left: 0; right: 0;
    background: var(--band);
  }
  .band--tagline {
    top: 214px; height: 30px;
    color: var(--band-text);
    font-size: 15px;
    letter-spacing: .5px;
    text-align: center;
    line-height: 30px;
  }
  .band--base { top: 392px; height: 34px; }

  .person {
    position: absolute;
    top: 292px;
    right: 470px;
    text-align: right;
  }
  .person__name { font-size: 27px; font-weight: 700; color: var(--ink); }
  .person__role { font-size: 16px; color: var(--ink-soft); margin-top: 2px; }

  .divider {
    position: absolute;
    left: 378px; top: 268px;
    width: 1px; height: 100px;
    background: var(--rule);
  }
  .contacts {
    position: absolute;
    left: 404px; top: 270px;
    list-style: none;
    font-size: 17px;
    color: var(--ink);
  }
  .contacts li {
    display: flex; align-items: center;
    gap: 12px;
    height: 32px;
  }
  .contacts svg { width: 15px; height: 15px; flex: none; }
  .icon-fill { fill: var(--band); }
  .icon-line { fill: none; stroke: var(--band); }
</style>
</head>
<body>
  <section class="card card--back" aria-label="Card back">
    <div class="leaf-art" role="img" aria-label="Cigar leaf illustration"></div>
    <h1 class="brand">Brevin Kaltwell</h1>
  </section>

  <section class="card card--front" aria-label="Card front">
    <div class="leaf-art" role="img" aria-label="Cigar leaf illustration"></div>
    <h2 class="brand">Brevin Kaltwell</h2>
    <div class="band band--tagline">Respect the smoke</div>

    <div class="person">
      <div class="person__name">Calvin Rusholm</div>
      <div class="person__role">Owner</div>
    </div>
    <div class="divider"></div>
    <ul class="contacts">
      <li>
        <svg viewBox="0 0 16 16"><path class="icon-fill" d="M3 1h3l1.5 4-2 1.3a9 9 0 0 0 4.2 4.2L11 8.5l4 1.5v3a2 2 0 0 1-2 2A12 12 0 0 1 1 3a2 2 0 0 1 2-2z"/></svg>
        614-587-3906
      </li>
      <li>
        <svg viewBox="0 0 16 16"><path class="icon-line" stroke-width="1.6" d="M1 3h14v10H1z M1 3l7 6 7-6"/></svg>
        crusholm@brevinleafco.com
      </li>
      <li>
        <svg viewBox="0 0 16 16"><circle class="icon-line" stroke-width="1.5" cx="8" cy="8" r="6.5"/><path class="icon-line" stroke-width="1.2" d="M1.5 8h13M8 1.5c-3 3.5-3 9.5 0 13M8 1.5c3 3.5 3 9.5 0 13"/></svg>
        www.brevinkaltwell.com
      </li>
    </ul>
    <div class="band band--base"></div>
  </section>
</body>
</html>
```